Home Baker of cakes, muffins, cookies and pastries.

I am looking for business cards for my home baking business called " Mmm Bex-O Plenty " - I want them to be super cute and girly, yet simple and modern at the same time. Pastel colours is what I envision with the main colour being baby pink.

```html
<!DOCTYPE html>
<html lang="en">
<head>
<meta charset="utf-8">
<title>Mmm Bex-O Plenty – Business Card</title>
<link rel="stylesheet" href="https://fonts.googleapis.com/css2?family=Arimo:wght@400&display=swap">
<style>
  :root {
    --pink: #e64e92;
    --pink-soft: #f1a3b5;
    --pink-faint: #f9dbe6;
    --pink-mist: #fcecf2;
    --paper: #ffffff;
  }
  * { margin: 0; padding: 0; box-sizing: border-box; }
  html, body { width: 1200px; height: 694px; overflow: hidden; background: var(--paper); }
  .card {
    position: relative;
    width: 1200px;
    height: 694px;
    background: var(--paper);
    font-family: "Arimo", Arial, sans-serif;
    color: var(--pink);
    overflow: hidden;
  }
  .decor-cupcake {
    position: absolute;
    left: 918px;
    top: 20px;
    width: 282px;
    height: 650px;
    background: linear-gradient(180deg, var(--pink-faint) 0%, var(--pink-mist) 60%, rgba(252,236,242,0.4) 100%);
    border-radius: 140px 0 0 40px;
  }
  .brand {
    position: absolute;
    left: 158px;
    top: 195px;
    font-size: 76px;
    line-height: 1;
    font-weight: 400;
    color: var(--pink);
    white-space: nowrap;
  }
  .person { position: absolute; left: 87px; top: 430px; }
  .person-name { font-size: 33px; line-height: 38px; color: var(--pink); }
  .person-role { font-size: 33px; line-height: 38px; color: var(--pink-soft); }
  .contact {
    position: absolute;
    left: 85px;
    top: 540px;
    list-style: none;
  }
  .contact-item {
    display: flex;
    align-items: center;
    height: 34px;
    margin-bottom: 13px;
    font-size: 25px;
  }
  .contact-icon { width: 24px; height: 24px; margin-right: 17px; flex: none; }
  .social {
    position: absolute;
    right: 94px;
    top: 587px;
    display: flex;
    align-items: center;
    font-size: 25px;
    height: 34px;
  }
  .social-dot {
    width: 20px;
    height: 20px;
    margin-left: 5px;
    border-radius: 50%;
    background: var(--pink);
  }
</style>
</head>
<body>
  <div class="card">
    <div class="decor-cupcake" role="img" aria-label="Faint pastel pink cupcake illustration decorating the right edge"></div>

    <div class="brand">Mmm Bex-O Plenty</div>

    <div class="person">
      <p class="person-name">Rebecca Hale</p>
      <p class="person-role">Patisserie Chef</p>
    </div>

    <ul class="contact">
      <li class="contact-item">
        <svg class="contact-icon" viewBox="0 0 24 24" aria-hidden="true">
          <circle cx="12" cy="12" r="10.5" fill="none" stroke="var(--pink)" stroke-width="2"/>
          <path d="M7 10.5c0-1.6 2.2-2.6 5-2.6s5 1 5 2.6v.6h-2.3v-1.3c-.8-.3-1.7-.4-2.7-.4s-1.9.1-2.7.4v1.3H7z" fill="var(--pink)"/>
          <rect x="8" y="11.5" width="8" height="4.5" rx="1" fill="var(--pink)"/>
        </svg>
        <span>0412555019</span>
      </li>
      <li class="contact-item">
        <svg class="contact-icon" viewBox="0 0 24 24" aria-hidden="true">
          <circle cx="12" cy="12" r="10.5" fill="none" stroke="var(--pink)" stroke-width="2"/>
          <rect x="6.5" y="8.5" width="11" height="7.5" rx="0.8" fill="var(--pink)"/>
          <path d="M6.8 9l5.2 4 5.2-4" fill="none" stroke="var(--paper)" stroke-width="1.1"/>
        </svg>
        <span>MmmBex-OPlenty@mailbox.com</span>
      </li>
    </ul>

    <div class="social">
      <span>mmm.bex.o.plenty</span>
      <span class="social-dot" aria-hidden="true"></span>
    </div>
  </div>
</body>
</html>
```